Book Cover Design - "Lanterns Seldom Wander"

Looking for an eye-catching but professional book cover.

This book is designed to help people figure out why they hate their job and what to do about it.

The audience for this book is 18-35 year olds who feel stuck in their current roles. The theory here is that people often wind up in a job they don't love, then settle because they don't realize they can make things better.

The writer's style is clever and balances humor with practical advice.

```html
<!DOCTYPE html>
<html lang="en">
<head>
<meta charset="utf-8">
<title>Lanterns Seldom Wander — Book Cover</title>
<link rel="stylesheet" href="https://fonts.googleapis.com/css2?family=Raleway:wght@200&family=Courier+Prime:wght@700&display=swap">
<style>
  :root {
    --page-bg: #ffffff;
    --cover-edge: #b8a6b0;
    --cover-glow: #e6dfe3;
    --title-ink: #2b2528;
    --author-ink: #2a2427;
    --art-warm: #f4bf16;
    --art-hot: #e52a22;
  }
  * { margin: 0; padding: 0; box-sizing: border-box; }
  html, body {
    width: 1200px;
    height: 1000px;
    overflow: hidden;
    background: var(--page-bg);
  }
  .canvas {
    width: 1200px;
    height: 1000px;
    display: flex;
    align-items: center;
    justify-content: center;
  }
  .book-cover {
    position: relative;
    width: 520px;
    height: 900px;
    background: radial-gradient(ellipse 62% 48% at 50% 46%, var(--cover-glow) 0%, #d2c5cc 45%, var(--cover-edge) 100%);
    box-shadow: 0 6px 24px rgba(0, 0, 0, 0.12);
  }
  .cover-title {
    position: absolute;
    top: 62px;
    left: 34px;
    font-family: "Raleway", "Helvetica Neue", sans-serif;
    font-weight: 200;
    color: var(--title-ink);
    text-transform: uppercase;
    line-height: 0.95;
    white-space: nowrap;
  }
  .cover-title .title-main {
    display: block;
    font-size: 66px;
    letter-spacing: 1px;
  }
  .cover-title .title-sub {
    display: block;
    margin-left: 30px;
    font-size: 38px;
    letter-spacing: 1px;
  }
  .cover-art {
    position: absolute;
    top: 310px;
    left: 50%;
    width: 220px;
    height: 190px;
    transform: translateX(-50%);
    background: radial-gradient(ellipse at 50% 60%, var(--art-warm) 0%, var(--art-warm) 40%, var(--art-hot) 100%);
  }
  .cover-author {
    position: absolute;
    bottom: 150px;
    left: 0;
    right: 0;
    text-align: center;
    font-family: "Courier Prime", "Courier New", monospace;
    font-weight: 700;
    font-size: 17px;
    letter-spacing: 1px;
    color: var(--author-ink);
  }
</style>
</head>
<body>
  <main class="canvas">
    <section class="book-cover">
      <h1 class="cover-title">
        <span class="title-main">Lanterns</span>
        <span class="title-sub">Seldom Wander</span>
      </h1>

      <div class="cover-art" role="img" aria-label="Illustration: red and yellow triangular warning sign showing a figure slumped back with feet up"></div>

      <p class="cover-author">by writer name</p>
    </section>
  </main>
</body>
</html>
```